Veltrano - Mechanic/Collision Center Business Card

We're looking for a business card design for our mechanic/ collision repair shop.

Can be with colours or monochromatic.

See the attached files.

Many thanks

```html
<!DOCTYPE html>
<html lang="en">
<head>
<meta charset="utf-8">
<title>Veltrano – Business Card</title>
<link href="https://fonts.googleapis.com/css2?family=Exo+2:wght@400;600;800&display=swap" rel="stylesheet">
<style>
  :root{
    --stage:#262626;
    --card-dark:#0d0f11;
    --card-mid:#1b2126;
    --steel:#2a3640;
    --accent:#2aa3e0;
    --white:#f4f6f8;
    --muted:#c9cfd4;
    --swoosh:#3a4046;
  }
  *{margin:0;padding:0;box-sizing:border-box}
  html,body{width:1200px;height:880px;overflow:hidden;background:var(--stage)}
  body{position:relative;font-family:"Exo 2",sans-serif;color:var(--white)}

  .card{position:absolute;width:560px;height:320px;border-radius:4px;overflow:hidden;
        box-shadow:0 14px 30px rgba(0,0,0,.55)}
  .card-front{left:60px;top:70px}
  .card-back{left:580px;top:490px}

  .texture{position:absolute;inset:0}
  .card-front .texture{
    background:linear-gradient(120deg,#0a1014 0%,#1d3442 30%,#0b1216 50%,#24404f 72%,#0a0f12 100%);
  }
  .card-back .texture{
    background:linear-gradient(150deg,#1c1f22 0%,#121416 45%,#0b0c0d 100%);
  }
  .swoosh{position:absolute;inset:0;width:100%;height:100%}

  .wordmark{position:absolute;display:flex;align-items:center;gap:12px;
            font-weight:800;text-transform:uppercase;letter-spacing:2px;line-height:1}
  .wordmark .mark{display:block;background:var(--accent)}
  .card-front .wordmark{left:50%;top:50%;transform:translate(-50%,-50%);
            font-size:52px;color:var(--muted)}
  .card-front .wordmark .mark{width:26px;height:26px;background:var(--muted)}
  .card-back .wordmark{right:38px;top:64px;font-size:40px;color:var(--white)}
  .card-back .wordmark .mark{width:20px;height:20px}

  .person{position:absolute;left:34px;top:150px}
  .person-name{font-weight:800;font-size:17px;letter-spacing:1px;text-transform:uppercase}
  .person-role{font-weight:400;font-size:14px;letter-spacing:.5px;color:var(--accent);text-transform:uppercase}

  .contact{position:absolute;left:34px;bottom:26px;list-style:none;font-size:14px;line-height:1.35}
  .contact li{display:flex;align-items:flex-start;gap:10px}
  .contact .icon{flex:none;width:16px;height:16px;margin-top:2px;border-radius:3px;background:var(--accent);
                 display:flex;align-items:center;justify-content:center}
  .contact .icon svg{width:11px;height:11px;fill:var(--white)}
</style>
</head>
<body>

<section class="card card-front" aria-label="Card front">
  <div class="texture" role="img" aria-label="Dark blue carbon fibre texture with light sheen"></div>
  <div class="wordmark"><span class="mark"></span>Veltrano</div>
</section>

<section class="card card-back" aria-label="Card back">
  <div class="texture" role="img" aria-label="Dark carbon fibre texture"></div>
  <svg class="swoosh" viewBox="0 0 560 320" preserveAspectRatio="none" aria-hidden="true">
    <path d="M0 150 C140 90 300 110 560 10 L560 0 L0 0 Z" fill="#181b1e" opacity=".7"/>
    <path d="M0 150 C150 95 310 120 560 30" fill="none" stroke="var(--swoosh)" stroke-width="3"/>
    <path d="M180 320 C260 250 420 220 560 150 L560 320 Z" fill="#2b3035" opacity=".55"/>
    <path d="M240 320 C320 265 440 235 560 185" fill="none" stroke="#4a5157" stroke-width="2"/>
  </svg>

  <div class="wordmark"><span class="mark"></span>Veltrano</div>

  <div class="person">
    <p class="person-name">Rui Marques</p>
    <p class="person-role">Managing Director</p>
  </div>

  <ul class="contact">
    <li><span class="icon"><svg viewBox="0 0 24 24"><path d="M6.6 10.8a15 15 0 0 0 6.6 6.6l2.2-2.2c.3-.3.7-.4 1-.2 1.1.4 2.3.6 3.6.6.6 0 1 .4 1 1V20c0 .6-.4 1-1 1C10.6 21 3 13.4 3 4c0-.6.4-1 1-1h3.5c.6 0 1 .4 1 1 0 1.3.2 2.5.6 3.6.1.3 0 .7-.2 1z"/></svg></span>+351 210 004 417</li>
    <li><span class="icon"><svg viewBox="0 0 24 24"><path d="M2 5h20v14H2z M4 7v.5l8 5 8-5V7l-8 5z" fill-rule="evenodd"/></svg></span>veltrano.mail@example.com</li>
    <li><span class="icon"><svg viewBox="0 0 24 24"><circle cx="12" cy="12" r="9" fill="none" stroke="#f4f6f8" stroke-width="2.5"/><path d="M3 12h18M12 3c3 3 3 15 0 18M12 3c-3 3-3 15 0 18" fill="none" stroke="#f4f6f8" stroke-width="2"/></svg></span>www.veltrano-auto.pt</li>
    <li><span class="icon"><svg viewBox="0 0 24 24"><path d="M12 2a7 7 0 0 0-7 7c0 5 7 13 7 13s7-8 7-13a7 7 0 0 0-7-7zm0 9.5A2.5 2.5 0 1 1 12 6.5a2.5 2.5 0 0 1 0 5z"/></svg></span>Rua das Oficinas, 42<br>1950-118 Lisboa</li>
  </ul>
</section>

</body>
</html>
```